Info flyer to showcase security camera install and remote video monitoring.

I am looking for an attractive looking flyer that is simple and has some text content and some photos to show prospective clients what services I can provide them.

The two main services that I want to showcase are:
1. Security Camera & NVR Installations and maintenance
2. Remote Video Monitoring for business. This can be a temporary service or ongoing/long term.

Target Market(s)

Construction, Retail, Industrial, Commercial

Industry/Entity Type

Security

Font styles to use
Serif

Colors

Designer to choose colors to be used in the design.

```html
<!DOCTYPE html>
<html lang="en">
<head>
<meta charset="utf-8">
<title>Vantage Secure Systems – Security Flyer</title>
<link href="https://fonts.googleapis.com/css2?family=Roboto+Condensed:wght@700&family=Michroma&family=Lato:wght@400;700;900&display=swap" rel="stylesheet">
<style>
  :root {
    --gold: #c9a02c;
    --ink: #2b2b2b;
    --charcoal: #3a3a3a;
    --paper: #ffffff;
    --page: #ffffff;
    --sky-top: #2f7fd6;
    --sky-bottom: #5aa2ea;
    --mall-a: #cfd6de;
    --mall-b: #8fa2b6;
  }
  * { margin: 0; padding: 0; box-sizing: border-box; }
  html, body { width: 1200px; height: 1200px; overflow: hidden; background: var(--page); }
  .canvas { position: relative; width: 1200px; height: 1200px; }
  .flyer {
    position: absolute; left: 232px; top: 82px; width: 743px; height: 1040px;
    background: var(--paper); overflow: hidden;
  }
  .flyer-shapes { position: absolute; inset: 0; }
  .brand {
    position: absolute; left: 36px; top: 352px;
    color: var(--paper); font-family: "Lato", sans-serif; font-weight: 700;
  }
  .brand-name { font-size: 46px; line-height: 1; letter-spacing: 1px; }
  .brand-sub { display: block; font-size: 19px; line-height: 1; letter-spacing: 0.5px; margin-top: 8px; }
  .welcome { position: absolute; left: 22px; top: 570px; }
  .welcome-lead {
    font-family: "Roboto Condensed", sans-serif; font-weight: 700;
    font-size: 37px; color: var(--ink); line-height: 1;
  }
  .welcome-name {
    font-family: "Roboto Condensed", sans-serif; font-weight: 700;
    font-size: 50px; color: var(--gold); line-height: 1; margin-top: 8px;
  }
  .welcome-sub {
    font-family: "Michroma", sans-serif; font-size: 36px; color: var(--ink);
    line-height: 1; margin-top: 6px; letter-spacing: 1px;
    -webkit-text-stroke: 1.2px var(--ink);
  }
  .services-tag {
    position: absolute; left: 20px; top: 726px;
    font-family: "Roboto Condensed", sans-serif; font-weight: 700;
    font-size: 25px; color: var(--gold);
  }
  .services { position: absolute; left: 18px; top: 788px; list-style: none; width: 440px; }
  .services li {
    display: flex; gap: 9px; font-family: "Lato", sans-serif; font-size: 16px;
    color: var(--ink); line-height: 20px; margin-bottom: 9px;
  }
  .services .num {
    flex: none; width: 18px; height: 18px; border-radius: 50%; background: var(--gold);
    color: var(--ink); font-weight: 700; font-size: 12px; text-align: center; line-height: 18px;
    margin-top: 1px;
  }
  .call { position: absolute; left: 18px; top: 900px; display: flex; align-items: baseline; gap: 12px; }
  .call-label { font-family: "Roboto Condensed", sans-serif; font-weight: 700; font-size: 46px; color: var(--gold); }
  .call-number { font-family: "Roboto Condensed", sans-serif; font-weight: 700; font-size: 36px; color: var(--ink); }
  .website { position: absolute; left: 24px; top: 960px; font-family: "Lato", sans-serif; font-size: 16px; color: var(--ink); }
</style>
</head>
<body>
<div class="canvas">
  <div class="flyer">
    <svg class="flyer-shapes" width="743" height="1040" viewBox="0 0 743 1040">
      <defs>
        <linearGradient id="mallTone" x1="0" y1="0" x2="1" y2="1">
          <stop offset="0" stop-color="var(--mall-a)"/>
          <stop offset="0.6" stop-color="var(--mall-b)"/>
          <stop offset="1" stop-color="#d8dde2"/>
        </linearGradient>
        <linearGradient id="skyTone" x1="0" y1="0" x2="0" y2="1">
          <stop offset="0" stop-color="var(--sky-top)"/>
          <stop offset="1" stop-color="var(--sky-bottom)"/>
        </linearGradient>
        <linearGradient id="workTone" x1="0" y1="0" x2="1" y2="1">
          <stop offset="0" stop-color="#e6e9ec"/>
          <stop offset="1" stop-color="#3d5a8a"/>
        </linearGradient>
      </defs>

      <g role="img" aria-label="Photo of a dome security camera in a bright shopping centre">
        <rect x="0" y="0" width="743" height="470" fill="url(#mallTone)"/>
      </g>

      <polygon points="0,236 490,386 370,448 0,512" fill="var(--gold)"/>
      <polygon points="0,512 370,448 470,440 0,526" fill="var(--ink)"/>
      <polygon points="0,526 470,440 743,470 743,1040 0,1040" fill="var(--paper)"/>
      <polygon points="700,455 743,460 743,476 700,470" fill="var(--gold)"/>

      <g transform="translate(583 486)">
        <polygon points="53.6,-129.4 129.4,-53.6 129.4,53.6 53.6,129.4 -53.6,129.4 -129.4,53.6 -129.4,-53.6 -53.6,-129.4" fill="var(--charcoal)"/>
        <polygon points="50.5,-121.9 121.9,-50.5 121.9,50.5 50.5,121.9 -50.5,121.9 -121.9,50.5 -121.9,-50.5 -50.5,-121.9" fill="var(--gold)"/>
        <polygon role="img" aria-label="Photo of bullet security cameras mounted on a pole against blue sky" points="47.8,-115.4 115.4,-47.8 115.4,47.8 47.8,115.4 -47.8,115.4 -115.4,47.8 -115.4,-47.8 -47.8,-115.4" fill="url(#skyTone)"/>
      </g>

      <polygon points="0,726 288,726 268,756 0,756" fill="var(--charcoal)"/>

      <polygon points="310,1040 743,868 743,1040" fill="var(--gold)"/>
      <polygon points="0,1026 320,1026 300,1040 0,1040" fill="var(--charcoal)"/>
      <line x1="300" y1="1040" x2="500" y2="944" stroke="var(--ink)" stroke-width="3"/>

      <g transform="translate(590 881)">
        <polygon points="45,-108.7 108.7,-45 108.7,45 45,108.7 -45,108.7 -108.7,45 -108.7,-45 -45,-108.7" fill="var(--charcoal)"/>
        <polygon points="42.5,-102.6 102.6,-42.5 102.6,42.5 42.5,102.6 -42.5,102.6 -102.6,42.5 -102.6,-42.5 -42.5,-102.6" fill="var(--gold)"/>
        <polygon role="img" aria-label="Photo of a technician installing a security camera on a wall" points="40,-96.5 96.5,-40 96.5,40 40,96.5 -40,96.5 -96.5,40 -96.5,-40 -40,-96.5" fill="url(#workTone)"/>
      </g>
    </svg>

    <div class="brand">
      <p class="brand-name">VANTAGE</p>
      <p class="brand-sub">SECURE SYSTEMS</p>
    </div>

    <div class="welcome">
      <p class="welcome-lead">WELL COME TO</p>
      <p class="welcome-name">VANTAGE SECURE</p>
      <p class="welcome-sub">SYSTEMS</p>
    </div>

    <p class="services-tag">The two main services</p>
    <ul class="services">
      <li><span class="num">1</span><span>Security Camera &amp; NVR Installations and maintenance</span></li>
      <li><span class="num">2</span><span>Remote Video Monitoring for business. This can be a temporary service or ongoing/long term</span></li>
    </ul>

    <div class="call">
      <span class="call-label">CALL NOW</span>
      <span class="call-number">0123456789</span>
    </div>
    <p class="website">www.companywebsite.com</p>
  </div>
</div>
</body>
</html>
```